Website design for a private chef business

Need a website that is eye catching and with easy contact, newsletter signups and scheduling tool/calendar . Website is chefdw.com and geographic focus is The Woodlands, TX and Austin, TX. I cook all styles of cuisine so anything is possible and I'm a veteran of Afghanistan via the Vale Guard so if you could mention it's a veteran owned business

Target Market(s)

Affluent families and successful professionals in TheWoodlands, TX and Austin, TX

Industry/Entity Type

Business

Number of Pages Required

1 page

Requirements
Must have
• Eyecatching visuals
• Contact form
• Newsletter sign up
• Scheduling tool
Should not have
• N/a

```html
<!DOCTYPE html>
<html lang="en">
<head>
<meta charset="utf-8">
<title>chefdw – Private Chef</title>
<link rel="stylesheet" href="https://fonts.googleapis.com/css2?family=Lato:wght@300;400;700&family=Arimo:wght@400&family=Montserrat:wght@400;500&display=swap">
<style>
:root{
  --page-bg:#eeeeee;
  --panel:#ffffff;
  --wine:#6e2220;
  --wine-dark:#5c1515;
  --ink:#555555;
  --ink-soft:#777777;
  --line:#d6d6d6;
  --orange:#f08a24;
  --orange-text:#e07b22;
  --cal-head:#dfe3e8;
  --cal-grey:#c4c4c4;
}
*{box-sizing:border-box;margin:0;padding:0}
html,body{width:1010px;height:1200px;overflow:hidden}
body{background:var(--page-bg);font-family:"Arimo",Arial,sans-serif;color:var(--ink);position:relative}
.page{position:absolute;left:162px;top:0;width:685px;height:1200px;background:var(--panel)}
.abs{position:absolute}

/* header */
.logo{left:19px;top:19px;font-family:"Lato",sans-serif;font-weight:700;font-size:11px;line-height:14px;color:var(--wine);white-space:nowrap}
.nav{left:75px;top:13px;height:26px;display:flex;align-items:center;font-family:"Lato",sans-serif;font-size:7.5px;color:#444;white-space:nowrap}
.nav a{color:inherit;text-decoration:none;margin-right:23px}
.nav .active{background:var(--wine);color:#fff;height:26px;width:47px;display:flex;align-items:center;justify-content:center;margin-right:10px}
.header-contact{left:538px;top:14px;font-size:5.6px;color:#444;line-height:12.5px}
.header-contact div{display:flex;align-items:center;gap:7px}
.header-contact svg{width:8px;height:7px}

/* hero */
.hero{left:0;top:54px;width:685px;height:346px;overflow:hidden;
  background:
    radial-gradient(ellipse 130px 70px at 210px 270px,rgba(235,220,210,.85),transparent 75%),
    radial-gradient(ellipse 110px 60px at 160px 230px,rgba(120,40,30,.8),transparent 70%),
    radial-gradient(ellipse 70px 110px at 480px 120px,rgba(60,10,10,.9),transparent 70%),
    radial-gradient(ellipse 90px 120px at 100px 60px,rgba(150,120,100,.55),transparent 70%),
    radial-gradient(ellipse 140px 90px at 600px 280px,rgba(110,40,40,.7),transparent 70%),
    linear-gradient(160deg,#3b2a22 0%,#5a3328 45%,#3a1c18 100%)}
.hero-title{left:201px;top:120px;color:#fff;font-family:"Lato",sans-serif;white-space:nowrap}
.hero-title h1{font-weight:700;font-size:24px;line-height:31px;letter-spacing:.2px}
.hero-title p{font-weight:400;font-size:14.5px;line-height:16px;letter-spacing:.2px}
.signup{left:159px;top:287px;display:flex;align-items:center}
.signup .email{width:110px;height:32px;background:rgba(255,255,255,.85);font-size:4.5px;color:#999;padding:13px 0 0 12px}
.signup .subscribe{width:75px;height:32px;background:var(--wine);color:#fff;border:1px solid #c8a8a0;font-family:"Lato",sans-serif;font-size:13.5px;display:flex;align-items:center;justify-content:center}
.signup .join{margin-left:28px;width:140px;height:32px;background:rgba(255,255,255,.92);color:#444;border:1px solid #d9c8c2;font-family:"Lato",sans-serif;font-size:13.5px;display:flex;align-items:center;justify-content:center}

/* about */
.about-title{left:24px;top:417px;font-family:"Lato",sans-serif;font-weight:300;font-size:21px;color:var(--wine-dark)}
.about-rule{left:23px;top:455px;width:287px;height:2px;background:#ebebeb}
.about-rule span{display:block;width:72px;height:2px;background:#cfcfcf}
.about-text{left:21px;top:470px;width:645px;font-size:7.5px;line-height:12.7px;color:#555}
.about-text p+p{margin-top:12.5px}
.section-rule{left:0;top:600px;width:685px;height:2px;background:linear-gradient(#ececec,#fafafa)}

/* contact */
.contact-intro{left:29px;top:631px;font-family:"Lato",sans-serif;font-size:9px;color:#888}
.form-label{left:29px;font-family:"Lato",sans-serif;font-size:6.8px;color:#555}
.field{left:77px;width:195px;height:18px;border:1px solid #d8d8d8;background:#fff}
.submit{left:77px;top:861px;width:64px;height:18px;background:var(--orange);border:1px solid #d46f12;color:#fff;font-size:6.5px;display:flex;align-items:center;justify-content:center}
.office{left:282px;font-family:"Montserrat",sans-serif;font-size:6.5px;line-height:12.7px;color:#555;white-space:nowrap}
.office h3{font-family:"Lato",sans-serif;font-weight:400;font-size:7.8px;color:var(--orange-text);margin-bottom:3px}
.office .gap{height:8px}
.office-rule{left:282px;top:786px;width:116px;height:1px;background:#cfcfcf}

/* calendar */
.calendar{left:427px;top:616px;width:226px;height:264px;background:#fff;border:1px solid #d5d5d5;box-shadow:0 1px 3px rgba(0,0,0,.18)}
.calendar h2{position:absolute;left:0;top:13px;width:100%;text-align:center;font-family:"Lato",sans-serif;font-weight:700;font-size:16px;line-height:21px;color:var(--wine-dark);letter-spacing:.3px}
.cal-head{position:absolute;left:0;top:76px;width:100%;height:27px;background:var(--cal-head);display:flex;align-items:center;justify-content:space-between;padding:0 8px;font-family:"Montserrat",sans-serif;font-size:12.5px;letter-spacing:1.4px;color:#555}
.cal-head svg{width:7px;height:9px}
.cal-grid{position:absolute;left:0;top:103px;width:100%;display:grid;grid-template-columns:repeat(7,1fr);grid-auto-rows:32px}
.cal-grid span{border-right:1px solid #e0e0e0;border-bottom:1px solid #e0e0e0;display:flex;align-items:center;justify-content:center;font-family:"Montserrat",sans-serif;font-size:11.5px;color:#444}
.cal-grid span:nth-child(7n){border-right:none}
.cal-grid .muted{color:var(--cal-grey)}
.cal-grid .today{color:var(--orange-text);background:#fbf7f4;outline:1px solid #e5b8aa;outline-offset:-1px}

/* footer */
.footer{left:0;top:964px;width:685px;height:236px;background:var(--wine)}
.footer-text{left:90px;top:47px;width:255px;font-size:7.5px;line-height:12.7px;color:#fff}
.footer-text p+p{margin-top:12.5px}
.feed-title{left:438px;top:15px;font-size:7.5px;color:#fff}
.feed{left:438px;width:165px;font-size:7.5px;line-height:12.7px;color:#fff}
.stamp{display:inline-flex;align-items:center;gap:6px;margin-top:3px;height:13px;padding:0 6px 0 3px;background:#3d3d3d;border-radius:2px;font-size:5.2px;color:#fff}
.stamp i{width:8px;height:8px;border-radius:50%;background:#666;display:block}
.footer-rule{left:90px;top:193px;width:505px;height:1px;background:#b07a78}
.footer-rule span{position:absolute;left:0;top:-1px;width:72px;height:3px;background:#fff}
.copyright{left:90px;top:214px;font-size:5.8px;color:#fff}
.social{top:210px;width:11px;height:11px;border-radius:50%;background:#fff}
.to-top{left:582px;top:210px;width:13px;height:13px;background:#555;border-radius:2px;display:flex;align-items:center;justify-content:center}
.to-top svg{width:7px;height:5px}
</style>
</head>
<body>
<div class="page">

  <header>
    <div class="abs logo">chefdw</div>
    <nav class="abs nav">
      <a class="active" href="#">Home</a>
      <a href="#">Menues</a>
      <a href="#">About Us</a>
      <a href="#">FAQ's</a>
      <a href="#">Blog</a>
      <a href="#">Testimonials</a>
      <a href="#">Contact</a>
    </nav>
    <div class="abs header-contact">
      <div><svg viewBox="0 0 8 7"><path d="M0 2.2Q4 -0.6 8 2.2L7 3.4 5.6 2.6V1.8H2.4V2.6L1 3.4Z M1.6 3.6H6.4L7 6.6H1Z" fill="#444"/></svg>+1 240 55 8181</div>
      <div><svg viewBox="0 0 8 7"><rect x="0" y="1" width="8" height="5.5" fill="#444"/><path d="M0 1.2L4 4 8 1.2" stroke="#fff" stroke-width=".8" fill="none"/></svg>info@chefdw.com</div>
    </div>
  </header>

  <section class="abs hero" role="img" aria-label="Blurred restaurant photo: plated steak with vegetables and a glass of red wine on a candlelit table">
    <div class="abs hero-title">
      <h1>LOREM IPSUM IS SIMPLY<br>DUMMY TEXT OF THE</h1>
      <p>PRINTING AND TYPESETTING INDUSTRY.</p>
    </div>
    <div class="abs signup">
      <div class="email">type your email</div>
      <div class="subscribe">SubsScribe</div>
      <div class="join">Signup</div>
    </div>
  </section>

  <section>
    <h2 class="abs about-title">ABOUT LORIAL LIPSUM</h2>
    <div class="abs about-rule"><span></span></div>
    <div class="abs about-text">
      <p>Lorem Ipsum is simply dummy text of the printing and typesetting industry. Lorem Ipsum has been the industry's standard dummy text ever since the 1500s, when an unknown printer took a galley of type and scrambled it to make a type specimen book. It has survived not only five centuries, but also the leap into electronic typesetting, remaining essentially unchanged. It was popularised in the 1960s with the release of Letterform sheets containing Lorem Ipsum passages, and more recently with desktop publishing software like Pagewright Studio including versions of Lorem Ipsum.</p>
      <p>Lorem Ipsum is simply dummy text of the printing and typesetting industry. Lorem Ipsum has been the industry's standard dummy text ever since the 1500s, when an unknown printer took a galley of type and scrambled it to make a type specimen book. It has survived not only five centuries, but also the leap into electronic typesetting, remaining essentially unchanged. It was popularised in the 1960s with the release of Letterform sheets containing Lorem Ipsum passages, and more recently with desktop publishing software like Pagewright Studio including versions of Lorem Ipsum.</p>
    </div>
    <div class="abs section-rule"></div>
  </section>

  <section>
    <p class="abs contact-intro">Drop a line when you have a minute and let me know what's up. Take care.</p>
    <div class="abs form-label" style="top:695px">Name:</div>
    <div class="abs field" style="top:690px"></div>
    <div class="abs form-label" style="top:720px">Email:</div>
    <div class="abs field" style="top:715px"></div>
    <div class="abs form-label" style="top:745px">Subject:</div>
    <div class="abs field" style="top:740px"></div>
    <div class="abs form-label" style="top:771px">Message:</div>
    <div class="abs field" style="top:768px;height:86px"></div>
    <div class="abs submit">Submit</div>

    <div class="abs office" style="top:689px">
      <h3>Head Office</h3>
      Lorem Ipsum Dolor Sit Moon Avenue<br>No:11/21 Planet City, Earth
      <div class="gap"></div>
      Fax: +555 797 534 01<br>Tel: +555 636 646 62<br>E-mail: name@domain.com
    </div>
    <div class="abs office-rule"></div>
    <div class="abs office" style="top:798px">
      <h3>Branch Office</h3>
      Lorem Ipsum Dolor Sit Moon Avenue<br>No:11/21 Planet City, Earth
      <div class="gap"></div>
      Fax: +555 797 534 01<br>Tel: +555 636 646 62
    </div>

    <div class="abs calendar">
      <h2>SCHEDULING<br>CALENDAR</h2>
      <div class="cal-head">
        <svg viewBox="0 0 7 9"><path d="M5.5 1L2 4.5 5.5 8" stroke="#666" stroke-width="1.4" fill="none"/></svg>
        NOVEMBER
        <svg viewBox="0 0 7 9"><path d="M1.5 1L5 4.5 1.5 8" stroke="#666" stroke-width="1.4" fill="none"/></svg>
      </div>
      <div class="cal-grid">
        <span class="muted">29</span><span class="muted">30</span><span class="muted">31</span><span>1</span><span>2</span><span>3</span><span>4</span>
        <span>5</span><span>6</span><span>7</span><span>8</span><span>9</span><span>10</span><span>11</span>
        <span>12</span><span>13</span><span>14</span><span>15</span><span>16</span><span>17</span><span>18</span>
        <span>19</span><span>20</span><span>21</span><span>22</span><span class="today">23</span><span>24</span><span>25</span>
        <span>26</span><span>27</span><span>28</span><span>29</span><span>30</span><span class="muted">1</span><span class="muted">2</span>
      </div>
    </div>
  </section>

  <footer class="abs footer">
    <div class="abs footer-text">
      <p>Lorem Ipsum is simply dummy text of the printing and typesetting industry. Lorem Ipsum has been the industry's standard dummy text ever since the 1500s, when an unknown printer took a galley of type and scrambled it to make a type specimen book. It has survived not only five centuries, but also the leap into electronic typesetting, remaining essentially unchanged.</p>
      <p>It was popularised in the 1960s with the release of Letterform sheets containing Lorem Ipsum passages, and more recently with desktop publishing software like Pagewright Studio including versions of Lorem Ipsum.</p>
    </div>
    <div class="abs feed-title">Chirpline</div>
    <div class="abs feed" style="top:52px">
      Skyrocket your event with elegant one-page responsive SitePress theme in.<br>
      <span class="stamp"><i></i>57 minutes ago</span>
    </div>
    <div class="abs feed" style="top:108px">
      Check this powerful full-width featured homepage slider with must-see.<br>
      <span class="stamp"><i></i>57 minutes ago</span>
    </div>
    <div class="abs footer-rule"><span></span></div>
    <div class="abs copyright">Copyright ©. All Rights Reserved.</div>
    <div class="abs social" style="left:528px" aria-label="Social link"></div>
    <div class="abs social" style="left:556px" aria-label="Social link"></div>
    <div class="abs to-top"><svg viewBox="0 0 7 5"><path d="M1 4L3.5 1.5 6 4" stroke="#fff" stroke-width="1.2" fill="none"/></svg></div>
  </footer>

</div>
</body>
</html>
```